Design Hybrid Mobile App (React Native)

Design hybrid mobile app for both iOS and Android.

Application design should utilize React Native design libraries and elements, and should have all sufficient aspects of application features and functionalities to direct developer to fully develop an MVP, i.e. error/invalid/valid messages, all case scenarios... etc.

Design needs to be optimized for and follow latest Apple and Android device sizes and should be provided in Adobe Experience or Sketch design format, and all elements need to be vectors.

Designs need to be provided with free stock images, animations for page transitions need to be provided portray UX.

A full library of colors, buttons and design elements should be provided in one files as well. Future roadmap of design elements (style guide, including fonts and branding required).

Minimal text entry in design, use of modern form elements (e.g. sliders), modern look required.
Updates

Need extra days to review

Font styles to use
Sans Serif

Colors

Designer to choose colors to be used in the design.

Requirements
Must have
• Experience/UX built around it, not just buttons and screens

```html
<!DOCTYPE html>
<html lang="en">
<head>
<meta charset="utf-8">
<title>Forkly – Food Quest App Screens</title>
<link rel="stylesheet" href="https://fonts.googleapis.com/css2?family=Josefin+Sans:wght@300;400;600&display=swap">
<style>
  :root {
    --bg: #e4eef0;
    --screen: #ffffff;
    --blue: #29a9e8;
    --blue-soft: #5cc3f2;
    --ink: #3a3f45;
    --muted: #9aa3ab;
    --line: #e7ecef;
    --red: #f0525a;
    --green: #3cc48a;
    --star: #f5b82e;
    --dark: #1d2226;
    --food-warm: linear-gradient(135deg, #5b3a26 0%, #8d4f2c 40%, #c9823f 70%, #3e5f2c 100%);
    --food-green: linear-gradient(135deg, #2f4a26 0%, #6d8f3a 45%, #d9c27a 80%, #7a3b24 100%);
    --food-grill: linear-gradient(135deg, #3a2418 0%, #a8622e 45%, #e0a155 75%, #4b2d1c 100%);
    --table: linear-gradient(160deg, #2e4a63 0%, #4c6b86 40%, #6f8aa0 70%, #2a3f52 100%);
  }
  * { box-sizing: border-box; margin: 0; padding: 0; }
  html, body { width: 1200px; height: 750px; overflow: hidden; }
  body {
    background: var(--bg);
    font-family: "Josefin Sans", "Helvetica Neue", sans-serif;
    color: var(--ink);
  }
  .board {
    width: 1200px; height: 750px;
    display: grid;
    grid-template-columns: repeat(4, 196px);
    grid-template-rows: repeat(2, 346px);
    gap: 22px 44px;
    justify-content: center;
    align-content: center;
  }
  .screen {
    position: relative;
    background: var(--screen);
    border-radius: 18px;
    overflow: hidden;
    box-shadow: 0 14px 30px rgba(60, 100, 120, .16);
    font-size: 9px;
  }
  .photo { display: block; }
  .warm { background: var(--food-warm); }
  .green { background: var(--food-green); }
  .grill { background: var(--food-grill); }
  .shade::after { content: ""; }

  /* shared bits */
  .avatar {
    position: absolute; top: 14px; right: 14px;
    width: 18px; height: 18px; border-radius: 50%;
    background: linear-gradient(135deg, #c7a48a, #8a6a58);
    border: 2px solid #fff;
  }
  .btn {
    display: block; text-align: center; border-radius: 20px;
    font-size: 9px; font-weight: 600; padding: 8px 0;
  }
  .btn-blue { background: var(--blue); color: #fff; box-shadow: 0 4px 10px rgba(41,169,232,.35); }
  .btn-white { background: #fff; color: var(--blue); }
  .label { color: var(--muted); font-size: 6.5px; letter-spacing: .2px; }
  .fab {
    position: absolute; width: 26px; height: 26px; border-radius: 50%;
    background: var(--blue); display: flex; align-items: center; justify-content: center;
    box-shadow: 0 4px 10px rgba(41,169,232,.4);
  }
  .back {
    position: absolute; top: 14px; left: 12px;
    width: 22px; height: 22px; border-radius: 50%; background: #fff;
    display: flex; align-items: center; justify-content: center;
  }
  .hero {
    position: relative; height: 130px;
  }
  .hero-text {
    position: absolute; left: 14px; bottom: 30px; color: #fff;
  }
  .hero-kicker { font-size: 8px; letter-spacing: .4px; opacity: .9; }
  .hero-title { font-size: 15px; font-weight: 600; line-height: 1.1; margin-top: 4px; }
  .sheet {
    position: absolute; left: 10px; right: 10px; top: 108px;
    background: #fff; border-radius: 8px; padding: 12px;
    box-shadow: 0 6px 16px rgba(0,0,0,.08);
  }
  .stars { color: var(--star); font-size: 7px; letter-spacing: 1px; }

  /* login */
  .login { background: var(--dark); }
  .login-bg { position: absolute; inset: 0; background: var(--table); opacity: .85; }
  .login-body { position: absolute; inset: 0; display: flex; flex-direction: column; align-items: center; padding: 0 26px; }
  .brand-mark { margin-top: 96px; display: flex; align-items: center; gap: 6px; color: #fff; font-size: 22px; font-weight: 400; }
  .brand-dot { width: 10px; height: 10px; border-radius: 50%; background: #fff; }
  .login-prompt { margin-top: 70px; color: #fff; font-size: 9px; }
  .login-body .btn { width: 100%; margin-top: 8px; }
  .create { margin-top: 12px; color: #fff; font-size: 8px; text-decoration: underline; }

  /* home */
  .home { padding: 16px 12px; }
  .brand-small { color: var(--blue); font-size: 10px; font-weight: 600; }
  .greet { margin-top: 20px; font-size: 15px; line-height: 1.2; font-weight: 400; }
  .search {
    margin-top: 12px; display: flex; justify-content: space-between; align-items: center;
    padding: 7px 8px; border-radius: 4px; box-shadow: 0 3px 10px rgba(0,0,0,.08);
    color: var(--muted); font-size: 8px;
  }
  .section-title { margin-top: 14px; font-size: 8px; font-weight: 600; display: flex; gap: 4px; align-items: center; }
  .section-title .count { color: var(--muted); font-weight: 400; }
  .dot-blue { width: 4px; height: 4px; border-radius: 50%; background: var(--blue); }
  .tiles { display: flex; gap: 6px; margin-top: 6px; }
  .tile { position: relative; flex: 1; height: 62px; border-radius: 4px; overflow: hidden; }
  .tile span { position: absolute; left: 5px; bottom: 10px; color: #fff; font-size: 8px; font-weight: 600; }
  .tile .stars { position: absolute; left: 5px; bottom: 3px; font-size: 5px; }
  .tile.short { height: 44px; }

  /* quest setup */
  .stepper { display: flex; gap: 5px; justify-content: center; margin: 6px 0 12px; }
  .stepper i { width: 4px; height: 4px; border-radius: 50%; background: var(--line); }
  .stepper i.on { background: var(--blue); }
  .card-heading { text-align: center; font-size: 9px; font-weight: 600; }
  .field { margin-top: 8px; }
  .field-value { font-size: 13px; margin-top: 2px; display: flex; align-items: center; gap: 4px; }
  .field-row { display: flex; justify-content: space-between; align-items: flex-end; }
  .change { color: var(--blue); font-size: 7px; }
  .sub { color: var(--muted); font-size: 6.5px; margin-top: 2px; }

  /* review */
  .review-list { margin-top: 6px; }
  .review-list .field { margin-top: 5px; }
  .review-list .field-value { font-size: 10px; }

  /* chat */
  .resto-name { font-size: 9px; font-weight: 600; }
  .resto-addr { color: var(--muted); font-size: 6.5px; margin-top: 2px; }
  .actions { display: flex; justify-content: space-between; margin-top: 6px; font-size: 7.5px; font-weight: 600; }
  .award { color: var(--green); }
  .decline { color: var(--red); }
  .chat-area { position: absolute; left: 10px; right: 10px; top: 206px; }
  .bubble { display: inline-block; border-radius: 10px; padding: 5px 8px; font-size: 7px; line-height: 1.3; margin-top: 4px; max-width: 78%; }
  .bubble.out { background: var(--blue); color: #fff; float: right; clear: both; }
  .bubble.in { background: #f1f4f6; color: var(--ink); }
  .incoming { clear: both; display: flex; gap: 5px; align-items: flex-end; padding-top: 6px; }
  .mini-avatar { width: 14px; height: 14px; border-radius: 50%; background: linear-gradient(135deg, #b9a08c, #6e5a4c); flex: none; }
  .composer {
    position: absolute; left: 0; right: 0; bottom: 0; height: 30px; background: var(--blue);
    display: flex; align-items: center; gap: 6px; padding: 0 8px;
  }
  .composer .plus { width: 14px; height: 14px; border-radius: 50%; background: #fff; color: var(--blue); font-size: 10px; display: flex; align-items: center; justify-content: center; }
  .composer .input { flex: 1; background: #fff; border-radius: 10px; padding: 4px 8px; color: var(--muted); font-size: 7px; }

  /* profile */
  .topbar { display: flex; align-items: center; gap: 8px; padding: 16px 12px 0; font-size: 10px; }
  .portrait {
    width: 112px; height: 112px; border-radius: 50%; margin: 22px auto 0;
    background: radial-gradient(circle at 50% 40%, #d9dee2 0%, #b8c0c6 60%, #8f979d 100%);
    position: relative;
  }
  .portrait .add { position: absolute; right: 10px; bottom: 4px; width: 16px; height: 16px; border-radius: 50%; background: var(--blue); color: #fff; font-size: 11px; display: flex; align-items: center; justify-content: center; }
  .profile-name { text-align: center; font-size: 18px; margin-top: 12px; }
  .profile-sub { text-align: center; color: var(--muted); font-size: 8px; margin-top: 3px; }
  .gallery { display: flex; gap: 6px; padding: 14px 12px 0; }
  .gallery .photo { flex: 1; height: 60px; border-radius: 4px; }

  /* ongoing */
  .tabs { display: flex; margin: 12px 12px 0; border-bottom: 1px solid var(--line); }
  .tab { flex: 1; text-align: center; font-size: 7.5px; color: var(--muted); padding-bottom: 6px; }
  .tab.active { color: var(--blue); border-bottom: 2px solid var(--blue); }
  .quest-card { margin: 10px 12px 0; border-radius: 6px; overflow: hidden; box-shadow: 0 4px 12px rgba(0,0,0,.08); }
  .quest-card .photo { height: 70px; position: relative; }
  .quest-card .photo span { position: absolute; left: 8px; bottom: 6px; color: #fff; font-size: 10px; font-weight: 600; line-height: 1.1; }
  .quest-card .meta { padding: 6px 8px; display: flex; gap: 5px; align-items: flex-start; }

  /* list */
  .list { padding: 14px 12px 0; }
  .list-row { display: flex; gap: 8px; margin-bottom: 10px; align-items: stretch; }
  .list-row .photo { width: 92px; height: 62px; border-radius: 5px; position: relative; flex: none; }
  .list-row .photo span { position: absolute; left: 6px; bottom: 5px; color: #fff; font-size: 8px; font-weight: 600; line-height: 1.1; }
  .list-row .info { padding-top: 8px; }
</style>
</head>
<body>
<main class="board">

  <!-- Log in -->
  <section class="screen login" aria-label="Log in screen">
    <div class="login-bg" role="img" aria-label="Photo of a dining table with plates, sauces and drinks"></div>
    <div class="login-body">
      <div class="brand-mark"><span class="brand-dot"></span>Forkly</div>
      <p class="login-prompt">Log in as</p>
      <a class="btn btn-white">Foodie</a>
      <a class="btn btn-blue">Restaurant</a>
      <a class="create">Create an account</a>
    </div>
  </section>

  <!-- Home -->
  <section class="screen home" aria-label="Home screen">
    <div class="brand-small">Forkly</div>
    <div class="avatar" role="img" aria-label="User avatar photo"></div>
    <h1 class="greet">Hello, Mira.<br>What would you<br>like to eat?</h1>
    <div class="search">
      <span>Search</span>
      <svg width="10" height="10" viewBox="0 0 10 10"><path d="M1 5 L9 1 L6 9 L5 5 Z" fill="none" stroke="#29a9e8" stroke-width="1"/></svg>
    </div>
    <div class="section-title">Popular around Doha <i class="dot-blue"></i></div>
    <div class="tiles">
      <div class="tile green" role="img" aria-label="Photo of a fresh salad bowl"></div>
      <div class="tile warm" role="img" aria-label="Photo of grilled steak"><span>Steak Night</span><span class="stars">★★★★</span></div>
      <div class="tile grill" role="img" aria-label="Photo of a salad plate"><span>Salad</span><span class="stars">★★★★</span></div>
    </div>
    <div class="section-title">Recently Added <span class="count">16</span></div>
    <div class="tiles">
      <div class="tile short" style="background: linear-gradient(135deg,#6a5a4a,#c59a5a)" role="img" aria-label="Photo of a board game table"><span>Board Game Night</span></div>
      <div class="tile short" style="background: linear-gradient(135deg,#c99a86,#e6c6b0)" role="img" aria-label="Photo of a movie night setup"><span>Movie Night</span></div>
    </div>
    <div class="fab" style="right:12px; bottom:14px;">
      <svg width="12" height="12" viewBox="0 0 12 12"><path d="M2 2 H10 V8 H5 L3 10 V8 H2 Z" fill="#fff"/></svg>
    </div>
  </section>

  <!-- Quest setup -->
  <section class="screen" aria-label="Quest setup screen">
    <div class="hero warm" role="img" aria-label="Photo of steak with roasted vegetables">
      <div class="back"><svg width="9" height="9" viewBox="0 0 9 9"><path d="M8 4.5 H1 M4 1.5 L1 4.5 L4 7.5" fill="none" stroke="#29a9e8" stroke-width="1.2"/></svg></div>
      <div class="hero-text">
        <div class="hero-kicker">Let's Get Started</div>
        <div class="hero-title">Custom title for<br>food quests</div>
      </div>
    </div>
    <div class="sheet">
      <div class="card-heading">Quest Details</div>
      <div class="stepper"><i class="on"></i><i></i><i></i><i class="on"></i></div>
      <div class="field">
        <div class="label">Order by</div>
        <div class="field-value">Deliver <svg width="7" height="5" viewBox="0 0 7 5"><path d="M1 1 L3.5 4 L6 1" fill="none" stroke="#29a9e8" stroke-width="1"/></svg></div>
      </div>
      <div class="field">
        <div class="label">Location</div>
        <div class="field-row"><div class="field-value">My Location</div><span class="change">Change</span></div>
        <div class="sub">#48 Doha Qatar</div>
      </div>
      <a class="btn btn-blue" style="margin-top:16px;">Next</a>
    </div>
  </section>

  <!-- Quest review -->
  <section class="screen" aria-label="Quest details review screen">
    <div class="hero grill" role="img" aria-label="Photo of grilled steak with vegetables">
      <div class="avatar" role="img" aria-label="User avatar photo"></div>
      <div class="hero-text">
        <div class="hero-title">Custom title for<br>food quests</div>
      </div>
    </div>
    <div class="sheet">
      <div class="card-heading" style="text-align:left;">Quest Details</div>
      <div class="label" style="margin-top:2px;">Review info</div>
      <div class="review-list">
        <div class="field"><div class="label">Order for</div><div class="field-value">5 Person</div></div>
        <div class="field"><div class="label">Budget</div><div class="field-value">100-200 QAR</div></div>
        <div class="field"><div class="label">Date</div><div class="field-value">Feb 26, 2018</div></div>
        <div class="field"><div class="label">Time</div><div class="field-value">6:00 PM</div></div>
        <div class="field"><div class="label">Order by</div><div class="field-value">Deliver</div></div>
        <div class="field"><div class="label">Location</div><div class="field-value">My Location</div></div>
      </div>
    </div>
  </section>

  <!-- Chat / award -->
  <section class="screen" aria-label="Restaurant offer chat screen">
    <div class="hero green" role="img" aria-label="Photo of steak with fresh vegetables">
      <div class="back"><svg width="9" height="9" viewBox="0 0 9 9"><path d="M8 4.5 H1 M4 1.5 L1 4.5 L4 7.5" fill="none" stroke="#29a9e8" stroke-width="1.2"/></svg></div>
      <div class="hero-text">
        <div class="hero-kicker">Almost There</div>
        <div class="hero-title">Custom title for<br>food quests</div>
      </div>
    </div>
    <div class="sheet" style="padding:10px;">
      <div class="resto-name">Anatolia Grill House</div>
      <div class="resto-addr">14 Corniche Lane, Doha, Qatar</div>
      <div><span class="stars">★★★★</span> <span class="label">4.6 (55 Reviews)</span></div>
      <div class="actions"><span class="award">Award</span><span class="decline">Decline</span></div>
    </div>
    <div class="chat-area">
      <span class="bubble out">You've got some great recommendations from us</span>
      <span class="bubble out">looking forward</span>
      <div class="incoming">
        <span class="mini-avatar" role="img" aria-label="Restaurant avatar photo"></span>
        <span class="bubble in">That's amazing. Let me think about this.</span>
      </div>
    </div>
    <div class="composer">
      <span class="plus">+</span>
      <span class="input">Send a Message</span>
      <svg width="10" height="10" viewBox="0 0 10 10"><path d="M1 5 L9 1 L6 9 L5 5 Z" fill="#fff"/></svg>
    </div>
  </section>

  <!-- Profile -->
  <section class="screen" aria-label="Profile screen">
    <div class="topbar">
      <svg width="9" height="9" viewBox="0 0 9 9"><path d="M8 4.5 H1 M4 1.5 L1 4.5 L4 7.5" fill="none" stroke="#29a9e8" stroke-width="1.2"/></svg>
      <span>Profile</span>
    </div>
    <div class="portrait" role="img" aria-label="Profile portrait photo">
      <span class="add">+</span>
    </div>
    <div class="profile-name">Lena</div>
    <div class="profile-sub">#48 Doha Qatar</div>
    <div class="gallery">
      <div class="photo grill" role="img" aria-label="Photo of grilled chicken"></div>
      <div class="photo green" role="img" aria-label="Photo of a salad dish"></div>
    </div>
  </section>

  <!-- Ongoing quests -->
  <section class="screen" aria-label="Ongoing quests screen">
    <div class="topbar">
      <svg width="9" height="9" viewBox="0 0 9 9"><path d="M8 4.5 H1 M4 1.5 L1 4.5 L4 7.5" fill="none" stroke="#29a9e8" stroke-width="1.2"/></svg>
      <span>Ongoing Quests</span>
    </div>
    <div class="avatar" role="img" aria-label="User avatar photo"></div>
    <div class="tabs"><span class="tab">In Progress</span><span class="tab active">Awarded</span></div>
    <article class="quest-card">
      <div class="photo grill" role="img" aria-label="Photo of grilled chicken"><span>Custom title for<br>food Quest</span></div>
      <div class="meta">
        <svg width="7" height="9" viewBox="0 0 7 9"><path d="M3.5 8.5 C1 5.5 0.5 4.5 0.5 3.5 A3 3 0 0 1 6.5 3.5 C6.5 4.5 6 5.5 3.5 8.5 Z" fill="#29a9e8"/></svg>
        <div><div class="resto-name" style="color:var(--blue)">Anatolia Grill House</div><div class="resto-addr">14 Corniche Lane, Doha, Qatar</div></div>
      </div>
    </article>
    <article class="quest-card">
      <div class="photo warm" role="img" aria-label="Photo of a wrap platter"><span>Custom title for<br>food Quest</span></div>
      <div class="meta">
        <svg width="7" height="9" viewBox="0 0 7 9"><path d="M3.5 8.5 C1 5.5 0.5 4.5 0.5 3.5 A3 3 0 0 1 6.5 3.5 C6.5 4.5 6 5.5 3.5 8.5 Z" fill="#29a9e8"/></svg>
        <div><div class="resto-name" style="color:var(--blue)">Lotus Thai Kitchen</div><div class="resto-addr">Doha, Qatar</div></div>
      </div>
    </article>
    <div class="fab" style="right:12px; bottom:12px;">
      <svg width="11" height="11" viewBox="0 0 11 11"><path d="M1.5 5.5 L5.5 2 L9.5 5.5 V9.5 H1.5 Z" fill="#fff"/></svg>
    </div>
  </section>

  <!-- Restaurant offers -->
  <section class="screen" aria-label="Restaurant offers list screen">
    <div class="list">
      <div class="list-row">
        <div class="photo grill" role="img" aria-label="Photo of grilled chicken"></div>
        <div class="info"><div class="resto-name">Lotus Thai Kitchen</div><div class="resto-addr">14 Corniche Lane, Doha, Qatar</div></div>
      </div>
      <div class="list-row">
        <div class="photo green" role="img" aria-label="Photo of a pizza"><span>Custom title for<br>food Quest</span></div>
        <div class="info"><div class="resto-name">Silver Spoon</div><div class="resto-addr">Doha, Qatar</div><div class="resto-addr">14 Corniche Lane</div></div>
      </div>
      <div class="list-row">
        <div class="photo warm" role="img" aria-label="Photo of grilled steak"><span>Custom title for<br>food Quest</span></div>
        <div class="info"><div class="resto-name">Lotus Thai Kitchen</div><div class="resto-addr">Doha, Qatar</div></div>
      </div>
      <div class="list-row">
        <div class="photo grill" role="img" aria-label="Photo of a grill platter"></div>
        <div class="info"><div class="resto-name">Silver Spoon</div><div class="resto-addr">Doha, Qatar</div></div>
      </div>
    </div>
    <div class="fab" style="right:12px; bottom:12px;">
      <svg width="11" height="11" viewBox="0 0 11 11"><path d="M1.5 5.5 L5.5 2 L9.5 5.5 V9.5 H1.5 Z" fill="#fff"/></svg>
    </div>
  </section>

</main>
</body>
</html>
```